Business Cards for new orthopaedic surgery practice

My husband and I are starting our own orthopaedic surgery practice. We are looking for a business card that is uniform, but one will have my name/title and the other will have his. You can just create one design with my name on it for now. But when I choose your design as the winning design I will ask that you add another copy with his name/title.

We are looking for classy, simple, elite all in one. We like dark blues/a little gold/yellow. Something that goes with our logo. We want our logo incorporated. Here is all the info you need:
Business name: RV Spine & Vitality Center
Location: 38915 North Bramble Ave
Palm Verda, FL 33999
Phone: 954-218-4630
Fax: 954-571-2846
Email: info@myrvspine.example

Names: Lucinda Ferrow, M.D.
Board Certified Hand and Upper Extremity Surgeon

Emeka Dlunga, M.D.
Board Certified Hip & Knee Replacement/General Orthopaedic Surgeon

Can decide what you want to put on the back. Maybe a slogan:
Steady Hands. Lasting Strength.

I am just going to upload our logo. The only thing is if we select you as the winning design, the location, and phone numbers may change. We will need your help to update that once fully solidified.

Industry/Entity Type

Medical

Contact Information for Business Card

Colors
0054AA
0677BA
7BADD7
CADEEF
E8F1F8
0094D4
00A9DD
6FCCEA
C7EBF8
E9F6FB

Requirements
Must have
• class, appeal,
Should not have
• We want to air on the side of masculine if we are looking at masculine vs. feminine feel. But we still want it classy, sophisticated, and something we will love

```html
<!DOCTYPE html>
<html lang="en">
<head>
<meta charset="utf-8">
<title>RV Spine &amp; Vitality Center – Business Card</title>
<link rel="stylesheet" href="https://fonts.googleapis.com/css2?family=Montserrat:wght@400;500;700&display=swap">
<style>
  :root {
    --stage: #3a3a3c;
    --navy: #1b2850;
    --navy-ink: #1c2a55;
    --gold: #c9a45c;
    --white: #ffffff;
    --grey-text: #3c3c44;
    --faint: #eceef2;
  }
  * { box-sizing: border-box; margin: 0; padding: 0; }
  html, body { width: 1200px; height: 689px; overflow: hidden; }
  body {
    background: var(--stage);
    font-family: "Montserrat", Arial, sans-serif;
    position: relative;
  }
  .card {
    position: absolute;
    top: 190px;
    width: 540px;
    height: 309px;
    border-radius: 24px;
    overflow: hidden;
  }
  .card-back { left: 40px; background: var(--navy); color: var(--white); }
  .back-mark {
    position: absolute;
    left: 50%; top: 42px;
    transform: translateX(-50%);
    width: 170px; height: 170px;
    border: 2px solid var(--white);
    border-radius: 50%;
    display: flex; align-items: center; justify-content: center;
    text-align: center;
  }
  .brand-name {
    font-weight: 500;
    font-size: 15px;
    letter-spacing: 2px;
    line-height: 1.5;
    text-transform: uppercase;
  }
  .slogan {
    position: absolute;
    left: 0; right: 0; top: 246px;
    text-align: center;
    font-size: 14px;
    letter-spacing: 0.5px;
  }
  .card-front { left: 620px; background: var(--white); color: var(--grey-text); }
  .faint-circle {
    position: absolute;
    left: -50px; top: 60px;
    width: 140px; height: 140px;
    border-radius: 50%;
    background: var(--faint);
  }
  .front-mark {
    position: absolute;
    right: 34px; top: 22px;
    width: 128px; height: 128px;
    border: 2px solid var(--gold);
    border-radius: 50%;
    display: flex; align-items: center; justify-content: center;
    text-align: center;
    color: var(--navy-ink);
  }
  .front-mark .brand-name { font-size: 11px; letter-spacing: 1.5px; }
  .person {
    position: absolute;
    left: 32px; top: 150px;
  }
  .person-name {
    color: var(--navy-ink);
    font-weight: 700;
    font-size: 26px;
    line-height: 1.1;
    margin-bottom: 6px;
  }
  .person-title { font-size: 12.5px; line-height: 1.45; }
  .contacts {
    position: absolute;
    left: 34px; top: 232px;
    list-style: none;
    font-size: 12.5px;
    line-height: 1.55;
  }
  .contacts li { display: flex; align-items: center; gap: 8px; }
  .contacts svg { width: 12px; height: 12px; fill: var(--navy-ink); flex: none; }
  .practice {
    position: absolute;
    right: 30px; top: 172px;
    text-align: right;
    font-size: 12.5px;
    line-height: 1.5;
    font-style: normal;
  }
  .practice-name { color: var(--navy-ink); font-weight: 500; font-size: 13.5px; }
</style>
</head>
<body>
  <section class="card card-back" aria-label="Card back">
    <div class="back-mark">
      <p class="brand-name">RV Spine &amp;<br>Vitality<br>Center</p>
    </div>
    <p class="slogan">Steady Hands. Lasting Strength.</p>
  </section>

  <section class="card card-front" aria-label="Card front">
    <div class="faint-circle" aria-hidden="true"></div>
    <div class="front-mark">
      <p class="brand-name">RV Spine &amp;<br>Vitality<br>Center</p>
    </div>

    <div class="person">
      <h1 class="person-name">Emeka Dlunga, M.D.</h1>
      <p class="person-title">Board Certified Hip &amp; Knee Replacement<br>General Orthopaedic Surgeon</p>
    </div>

    <ul class="contacts">
      <li>
        <svg viewBox="0 0 16 16" aria-label="Phone"><path d="M3.6 1.2l2.3 2.8-1.3 1.8c.9 2 2.5 3.6 4.5 4.5l1.8-1.3 2.8 2.3-1.2 2.6C7.3 14.3 1.7 8.7 1 3.5z"/></svg>
        <span>954-218-4630</span>
      </li>
      <li>
        <svg viewBox="0 0 16 16" aria-label="Fax"><path d="M4 1h8v4H4zM1 6h14v6h-3v3H4v-3H1zm4 4v4h6v-4z"/></svg>
        <span>954-571-2846</span>
      </li>
      <li>
        <svg viewBox="0 0 16 16" aria-label="Email"><path d="M1 3h14v1L8 9 1 4zm0 2.5l7 5 7-5V13H1z"/></svg>
        <span>info@myrvspine.example</span>
      </li>
    </ul>

    <address class="practice">
      <p class="practice-name">RV Spine &amp; Vitality Center</p>
      <p>38915 North Bramble Ave</p>
      <p>Palm Verda, FL 33999</p>
    </address>
  </section>
</body>
</html>
```